Buildora Speech for a trade show in Las Vegas

I've tried to create the powerpoint on my own. I used a template, but am not satisfied with the look and feel. I'd like something more professional looking. I need this powerpoint for an upcoming speech. I need the ppt to be in a format in which I can edit it for last-minute changes before my speech.

The Power Point has a lot of slides, but mostly I'm looking for a few good backgrounds so that every slide doesn't have to be completely unique. Plus, if you can clean up some of my graphics, that would be great too. Feel free to message me with any questions. Happy to help out.

Target Market(s)

Leaders in Construction and Manufacturing

Industry/Entity Type

Construction

Font styles to use
Sans Serif

Colors

Designer to choose colors to be used in the design.

Requirements
Must have
• The ability for me to edit the slides so that I can do some last-minute changes.
• I need to have the Buildora/BuilMix logo (small round logo) on the bottom of each slide (or at least most of them).
Nice to have
• Pictures of people on construction sites using heavy equipment. (Backhoes, Loaders, Tarrowfins, Trench Mole products, Grindlewyck products, Hollis Brandt products, etc)

```html
<!DOCTYPE html>
<html lang="en">
<head>
<meta charset="utf-8">
<title>Becoming a Construction Leader Worth Following</title>
<link rel="stylesheet" href="https://fonts.googleapis.com/css2?family=Montserrat:wght@500;700;800&display=swap">
<style>
  :root {
    --navy: #0f3e7c;
    --navy-deep: #123f80;
    --photo-light: #2a5a9a;
    --photo-dark: #14427f;
    --gold: #fbb21c;
    --white: #ffffff;
    --ink: #1b2a44;
  }
  html, body {
    margin: 0;
    padding: 0;
    width: 1200px;
    height: 900px;
    overflow: hidden;
    background: var(--white);
    font-family: "Montserrat", Arial, sans-serif;
  }
  .slide {
    position: relative;
    width: 1200px;
    height: 900px;
    overflow: hidden;
    background: var(--white);
  }
  .top-bar {
    position: absolute;
    left: 0; top: 0;
    width: 1200px;
    height: 80px;
    background: var(--white);
  }
  .deck-title {
    position: absolute;
    left: 30px;
    top: 17px;
    margin: 0;
    font-size: 33px;
    font-weight: 700;
    color: var(--navy);
    letter-spacing: 0;
  }
  .hero-photo {
    position: absolute;
    left: 0; top: 80px;
    width: 1200px;
    height: 752px;
    background:
      radial-gradient(ellipse at 75% 70%, rgba(80,130,190,0.55), transparent 55%),
      radial-gradient(ellipse at 20% 25%, rgba(60,105,170,0.5), transparent 50%),
      linear-gradient(180deg, var(--photo-light) 0%, var(--photo-dark) 100%);
  }
  .headline {
    position: absolute;
    left: 80px;
    top: 333px;
    margin: 0;
    font-size: 74px;
    line-height: 83px;
    font-weight: 800;
    text-transform: uppercase;
    color: var(--white);
  }
  .headline .accent { color: var(--gold); }
  .brand-badge {
    position: absolute;
    left: 1089px;
    top: 7px;
    width: 112px;
    height: 112px;
    border-radius: 50%;
    background: var(--white);
    display: flex;
    align-items: center;
    justify-content: center;
    text-align: center;
    font-size: 15px;
    font-weight: 700;
    color: var(--navy);
    line-height: 1.2;
  }
  .footer-bar {
    position: absolute;
    left: 0; top: 832px;
    width: 1200px;
    height: 68px;
    background: var(--navy-deep);
  }
  .footer-curve {
    position: absolute;
    left: 0; top: 820px;
  }
  .copyright {
    position: absolute;
    left: 24px;
    top: 854px;
    margin: 0;
    font-size: 21px;
    font-weight: 500;
    color: var(--white);
  }
  .page-number {
    position: absolute;
    left: 1070px;
    top: 854px;
    margin: 0;
    font-size: 21px;
    font-weight: 500;
    color: var(--ink);
  }
</style>
</head>
<body>
  <main class="slide">
    <header class="top-bar">
      <h2 class="deck-title">Persentation Title here</h2>
    </header>

    <div class="hero-photo" role="img" aria-label="Blue-toned photo of construction workers in hard hats looking up at a building under construction"></div>

    <h1 class="headline">
      Becoming a<br>
      <span class="accent">Construction Leader</span><br>
      Worth Following
    </h1>

    <div class="brand-badge">Buildora/<br>BuilMix</div>

    <footer>
      <div class="footer-bar"></div>
      <svg class="footer-curve" width="1200" height="80" viewBox="0 820 1200 80" aria-hidden="true">
        <path d="M918 900 C 990 850 1080 832 1200 830 L1200 900 Z" fill="var(--gold)"/>
        <path d="M902 900 C 980 843 1075 824 1200 822" fill="none" stroke="var(--white)" stroke-width="3"/>
      </svg>
      <p class="copyright">Copyright text here</p>
      <p class="page-number">Page : 01</p>
    </footer>
  </main>
</body>
</html>
```